Looking for attractive banner design (print banner)

I am looking to redesign a banner to be more attractive and professional. This will be a print banner, 24" x 36" vertical. I am attaching the original concept to reference. High resolution file for print required. fading or blurring the background, attractive fonts, gradient highlight for text boxes, etc.

```html
<!DOCTYPE html>
<html lang="en">
<head>
<meta charset="utf-8">
<title>Essential Oils for The Horse &amp; Rider</title>
<link href="https://fonts.googleapis.com/css2?family=Lobster&family=Roboto+Slab:wght@300&family=Roboto:wght@400;500;700;900&display=swap" rel="stylesheet">
<style>
  :root {
    --ink: #161616;
    --paper: #f5f5f5;
    --mist: #dcdcdc;
    --rule: #8a8a8a;
    --green-light: #4f9f4c;
    --green-mid: #2f7a35;
    --green-deep: #0f3d1a;
    --green-box: #1f5c2a;
    --yellow: #f5e617;
    --white: #ffffff;
    --black: #000000;
  }
  * { margin: 0; padding: 0; box-sizing: border-box; }
  html, body { width: 952px; height: 1200px; overflow: hidden; background: var(--paper); }
  .banner { position: relative; width: 952px; height: 1200px; font-family: "Roboto", sans-serif; color: var(--ink); overflow: hidden; }
  .backdrop { position: absolute; inset: 0; }
  .title { position: absolute; left: 44px; top: 18px; }
  .title-script { font-family: "Lobster", cursive; font-size: 70px; line-height: 1; letter-spacing: -1px; }
  .title-sub { font-family: "Roboto Slab", serif; font-weight: 300; font-size: 42px; line-height: 1; margin-top: -6px; margin-left: 2px; }
  .upper-list { position: absolute; left: 46px; top: 164px; width: 280px; }
  .group { padding-bottom: 14px; margin-bottom: 14px; border-bottom: 1px solid var(--rule); width: 230px; }
  .upper-list .group { width: 230px; min-height: 89px; }
  .upper-list .group:last-child { border-bottom: none; }
  .group h2 { font-weight: 500; font-size: 26px; line-height: 1.1; margin-bottom: 4px; white-space: nowrap; }
  .group p { font-size: 17px; line-height: 1.12; width: 280px; }
  .lower-grid { position: absolute; top: 755px; left: 46px; display: grid; grid-template-columns: 301px 301px 280px; row-gap: 0; color: var(--white); }
  .lower-grid .group { border-bottom-color: rgba(255,255,255,.45); min-height: 98px; margin-bottom: 8px; padding-bottom: 0; }
  .lower-grid .group.last { border-bottom: none; }
  .lower-grid .group p { width: 270px; }
  .disclaimer { position: absolute; left: 627px; top: 1073px; width: 276px; height: 89px; border-radius: 12px 12px 0 0; overflow: hidden; text-align: center; }
  .disclaimer-head { background: var(--green-box); color: var(--yellow); font-weight: 900; font-size: 24px; height: 40px; line-height: 40px; }
  .disclaimer-body { background: var(--white); color: var(--green-deep); font-weight: 700; font-size: 15px; line-height: 1.1; height: 49px; padding-top: 7px; }
  .contact-bar { position: absolute; left: 0; bottom: 0; width: 952px; height: 38px; background: var(--black); color: var(--white); display: flex; justify-content: center; align-items: center; gap: 28px; font-size: 15px; }
  .contact-item { display: flex; align-items: center; gap: 8px; }
  .dot { width: 14px; height: 14px; border-radius: 50%; border: 2px solid var(--white); }
</style>
</head>
<body>
<div class="banner">
  <svg class="backdrop" width="952" height="1200" viewBox="0 0 952 1200">
    <defs>
      <linearGradient id="sideMist" x1="0" y1="0" x2="1" y2="0">
        <stop offset="0" stop-color="#e6e6e6"/>
        <stop offset="1" stop-color="#f2f2f2"/>
      </linearGradient>
      <linearGradient id="pasture" x1="0" y1="0" x2="1" y2="1">
        <stop offset="0" stop-color="#8fa08a"/>
        <stop offset=".35" stop-color="#a4582a"/>
        <stop offset=".7" stop-color="#3f5a35"/>
        <stop offset="1" stop-color="#6b4a34"/>
      </linearGradient>
      <radialGradient id="foal" cx=".5" cy=".5" r=".5">
        <stop offset="0" stop-color="#8a3f1c"/>
        <stop offset=".7" stop-color="#9a4a22" stop-opacity=".7"/>
        <stop offset="1" stop-color="#9a4a22" stop-opacity="0"/>
      </radialGradient>
      <linearGradient id="meadow" x1="0" y1="0" x2="0" y2="1">
        <stop offset="0" stop-color="#4f9f4c"/>
        <stop offset=".45" stop-color="#347f38"/>
        <stop offset="1" stop-color="#0f3d1a"/>
      </linearGradient>
    </defs>
    <rect width="952" height="1200" fill="#f5f5f5"/>
    <g role="img" aria-label="Faded photo of a rider resting her head against a horse">
      <path d="M0 120 C120 150 260 200 330 300 L360 760 L0 760 Z" fill="url(#sideMist)"/>
    </g>
    <path d="M318 0 C395 110 400 260 440 380 C490 560 600 660 760 672 C850 676 910 660 952 640 L952 660 C900 690 820 700 760 696 C590 690 470 560 420 380 C385 250 380 110 300 0 Z" fill="#4a4a4a" opacity=".85"/>
    <g role="img" aria-label="Photo of a chestnut horse in a blue halter leaning over a wooden fence">
      <path d="M318 0 L952 0 L952 640 C910 660 850 676 760 672 C600 660 490 560 440 380 C400 260 395 110 318 0 Z" fill="url(#pasture)"/>
    </g>
    <path d="M0 610 C80 700 200 750 330 752 C420 752 470 700 560 700 C700 700 860 740 952 828 L952 1200 L0 1200 Z" fill="url(#meadow)"/>
    <g role="img" aria-label="Photo of a chestnut horse standing in profile">
      <ellipse cx="455" cy="790" rx="150" ry="200" fill="url(#foal)" opacity=".85"/>
    </g>
  </svg>

  <header class="title">
    <div class="title-script">Essential Oils for</div>
    <div class="title-sub">The Horse &amp; Rider</div>
  </header>

  <section class="upper-list">
    <div class="group"><h2>Brain</h2><p>Frankincense, Mind<br>Spark, Clear Path, Cedarwood</p></div>
    <div class="group"><h2>Skin &amp; Hair</h2><p>Cedarwood, Lavender,<br>Geranium, Frankincense, Myrrh</p></div>
    <div class="group"><h2>Ears</h2><p>Helichrysum, Fresh Field, Tea<br>Tree, Juniper</p></div>
    <div class="group"><h2>Lungs</h2><p>B.E., Kestrel, Eucalyptus, (all),<br>Stable Guard, Tea Tree, Blue Meadow</p></div>
    <div class="group"><h2>Muscles</h2><p>Easy Stride, Calm Reach,<br>Marjoram, Cypress,<br>Peppermint, Ridge Fir</p></div>
  </section>

  <section class="lower-grid">
    <div class="group"><h2>Immune Support</h2><p>Stable Guard, Oregano, Ocotea,<br>Long Trail, Lemon, Peppermint,<br>Cinnamon Bark, Rosemary</p></div>
    <div class="group"><h2>Eyes</h2><p>Frankincense, Sandalwood,<br>Carrot Seed, Lemongrass</p></div>
    <div class="group"><h2>Hormonal Balance</h2><p>Clare Sage, Moon Cycle,<br>Balance Flow, Myrtle, Blue Meadow</p></div>

    <div class="group"><h2>Tendons &amp; Ligaments</h2><p>Palo Santo, Lemongrass,<br>Rosemary, Peppermint</p></div>
    <div class="group"><h2>Mouth</h2><p>Clove, Ocotea, Tea Tree,<br>Wintergreen, Stable Guard</p></div>
    <div class="group"><h2>Bone &amp; Joints</h2><p>Ease Off, Helichrysum,<br>Wintergreen, Cool Brook, Steadfast</p></div>

    <div class="group"><h2>Hoof (Horse)</h2><p>Stable Guard, Tea Tree, Oregano,<br>Frankincense</p></div>
    <div class="group"><h2>Heart</h2><p>Orange, Ylang Ylang, Cypress,<br>Helichrysum, Palmarosa</p></div>
    <div class="group last"><h2>Feet (Rider)</h2><p>Rooted, Steadfast, Stable Guard,<br>Fresh Field, Oregano</p></div>

    <div class="group last"><h2>Emotional Support</h2><p>Steadfast, Solace, Open Sky,<br>Bright Day, Lemon</p></div>
    <div class="group last"><h2>Digestion</h2><p>Gut Ease, Soft Breeze, Ginger,<br>Fennel, Peppermint</p></div>
  </section>

  <aside class="disclaimer">
    <div class="disclaimer-head">DISCLAIMER</div>
    <div class="disclaimer-body">NOT EVALUATED BY THE FDA,<br>NOT MEDICAL ADVICE.</div>
  </aside>

  <footer class="contact-bar">
    <span class="contact-item"><span class="dot"></span>@meadowoilsequine</span>
    <span class="contact-item">
      <svg width="14" height="16" viewBox="0 0 14 16"><path d="M3 1 L6 1 L7 5 L5 6.5 C6 9 7.5 10.5 9.5 11.5 L11 9.5 L14 11 L13.5 14.5 C7 15 1 9 1.5 2.5 Z" fill="#fff"/></svg>
      555.010.2244
    </span>
    <span class="contact-item">
      <svg width="20" height="14" viewBox="0 0 20 14"><rect x="1" y="1" width="18" height="12" fill="none" stroke="#fff" stroke-width="1.6"/><path d="M1 1 L10 8 L19 1 M1 13 L7.5 6.5 M19 13 L12.5 6.5" fill="none" stroke="#fff" stroke-width="1.4"/></svg>
      hello@meadowoilsequine.com
    </span>
  </footer>
</div>
</body>
</html>
```